Bespoke Builders Business Card Design

We need a business card for an established builder of high quality bespoke homes in Auckland and Northland. We build and renovate homes collaboratively facilitating effective communication between owners, builders, architects, suppliers and tradespeople. We have never built or renovated a home that leaks or has faults. We only use reliable materials. We have never been sued or had legal action taken against us. We are honest builders of bespoke homes not group mass produced homes. Our niche market is in character homes. We practice sustainability and have built a lot of coastal property. We have been in business for over thirty years . We would like to see natural colors of the environment sand,sea and maybe vegetation . The design should communicate quality, sustainability,fair pricing, open communication and the originality of bespoke building. And the fact that the builder is registered.

Business

Dale Morvick Builders
Ph. 021583917
58 Harlow Rd Kerrigan Bay Auckland 0915
PO Box 287 Tawharu 0563

```html
<!DOCTYPE html>
<html lang="en">
<head>
<meta charset="utf-8">
<title>Dale Morvick Builders – Business Card</title>
<link rel="stylesheet" href="https://fonts.googleapis.com/css2?family=Bodoni+Moda:opsz,wght@6..96,400;6..96,700&display=swap">
<style>
  :root {
    --canvas-bg: #e9e6e1;
    --card-front: #050505;
    --card-back: #a8a8a8;
    --ink-light: #f2f2f2;
    --ink-dark: #111111;
    --rule: #d8d8d8;
  }
  * { box-sizing: border-box; margin: 0; padding: 0; }
  html, body {
    width: 1200px;
    height: 902px;
    overflow: hidden;
  }
  body {
    background: var(--canvas-bg);
    display: flex;
    flex-direction: column;
    align-items: center;
    justify-content: center;
    gap: 40px;
    font-family: "Bodoni Moda", "Didot", serif;
  }
  .card {
    width: 640px;
    height: 390px;
    border-radius: 4px;
    box-shadow: 0 10px 28px rgba(0,0,0,0.22);
    position: relative;
  }
  .card--front {
    background: var(--card-front);
    color: var(--ink-light);
    padding: 52px 44px 40px;
    display: flex;
    flex-direction: column;
    align-items: center;
  }
  .card__name {
    font-weight: 700;
    font-size: 56px;
    line-height: 1;
    letter-spacing: 0.01em;
    white-space: nowrap;
    text-shadow: 0 0 6px rgba(255,255,255,0.35);
  }
  .card__rule {
    width: 100%;
    height: 2px;
    background: var(--rule);
    margin-top: 14px;
  }
  .card__phone {
    margin-top: 30px;
    font-size: 26px;
    font-weight: 400;
    letter-spacing: 0.02em;
  }
  .card__address {
    margin-top: auto;
    text-align: center;
    font-size: 25px;
    line-height: 1.3;
    font-weight: 400;
    text-shadow: 0 0 4px rgba(255,255,255,0.25);
  }
  .card__address span { display: block; white-space: nowrap; }
  .card--back {
    background: var(--card-back);
    color: var(--ink-dark);
    display: flex;
    align-items: center;
    justify-content: center;
  }
  .card--back .card__name {
    text-shadow: 0 2px 4px rgba(0,0,0,0.25);
  }
</style>
</head>
<body>
  <section class="card card--front" aria-label="Business card front">
    <h1 class="card__name">Dale Morvick Builders</h1>
    <div class="card__rule"></div>
    <p class="card__phone">021583917</p>
    <address class="card__address">
      <span>58 Harlow Rd Kerrigan Bay Auckland 0915</span>
      <span>PO Box 287 Tawharu 0563</span>
    </address>
  </section>

  <section class="card card--back" aria-label="Business card back">
    <p class="card__name">Dale Morvick Builders</p>
  </section>
</body>
</html>
```